Business cards design on a high standard

We advise clients on insurance and financial matters, since these clients pay for our advice, the design should have a high standard. Our logo should be included. From the colors we are open for everything.

Colors

Designer to choose colors to be used in the design.

```html
<!DOCTYPE html>
<html lang="en">
<head>
<meta charset="utf-8">
<title>Alpine Counsel — Business Cards</title>
<link href="https://fonts.googleapis.com/css2?family=Roboto:wght@400;500;700&display=swap" rel="stylesheet">
<style>
  :root {
    --stage: #ecebe8;
    --card-front: #9a9ba0;
    --card-back: #1b1c1e;
    --brand-red: #e01b22;
    --text-light: #ffffff;
    --text-muted: #b9babd;
    --rule: #6d6e72;
  }
  * { margin: 0; padding: 0; box-sizing: border-box; }
  html, body {
    width: 1200px; height: 960px; overflow: hidden;
    background: var(--stage);
    font-family: "Roboto", Arial, sans-serif;
  }
  .stage { position: relative; width: 1200px; height: 960px; }
  .card {
    position: absolute; left: 250px; width: 700px; height: 400px;
    border-bottom: 4px solid var(--brand-red);
    border-left: 2px solid var(--brand-red);
    box-shadow: 0 10px 24px rgba(0,0,0,0.18);
  }
  .card--front { top: 50px; background: var(--card-front); }
  .card--back  { top: 500px; background: var(--card-back); }

  .wordmark {
    color: var(--brand-red); font-weight: 700; letter-spacing: 2px;
    text-transform: uppercase; white-space: nowrap;
  }
  .card--front .wordmark {
    position: absolute; left: 0; right: 0; top: 150px;
    text-align: center; font-size: 54px;
  }
  .website {
    position: absolute; left: 0; right: 0; top: 300px; text-align: center;
    color: var(--text-light); font-size: 15px; letter-spacing: 6px;
  }
  .card--back .wordmark {
    position: absolute; right: 40px; top: 70px; font-size: 40px;
  }
  .rule { position: absolute; height: 1px; background: var(--rule); }
  .rule--top { left: 320px; right: 40px; top: 185px; }
  .rule--bottom { left: 80px; right: 40px; top: 340px; }

  .person { position: absolute; left: 40px; top: 230px; }
  .person__name { color: var(--brand-red); font-weight: 700; font-size: 26px; line-height: 1.1; }
  .person__title { color: var(--text-muted); font-weight: 700; font-size: 20px; }

  .contact { position: absolute; list-style: none; }
  .contact--phones { left: 64px; top: 290px; }
  .contact--office { left: 270px; top: 240px; }
  .contact li {
    display: flex; align-items: center; gap: 8px;
    color: var(--text-muted); font-size: 16px; line-height: 22px;
  }
  .contact svg { width: 14px; height: 14px; fill: var(--brand-red); flex: none; }
  .address { left: 80px; top: 354px; }
</style>
</head>
<body>
<main class="stage">
  <section class="card card--front">
    <div class="wordmark">Alpine Counsel</div>
    <div class="website">www.alpinecounsel.com</div>
  </section>

  <section class="card card--back">
    <div class="wordmark">Alpine Counsel</div>
    <div class="rule rule--top"></div>

    <div class="person">
      <div class="person__name">Daniel Hartmann</div>
      <div class="person__title">President</div>
    </div>

    <ul class="contact contact--phones">
      <li><svg viewBox="0 0 24 24"><path d="M6.6 10.8a15 15 0 0 0 6.6 6.6l2.2-2.2c.3-.3.7-.4 1-.2 1.1.4 2.3.6 3.6.6.6 0 1 .4 1 1V20c0 .6-.4 1-1 1A17 17 0 0 1 3 4c0-.6.4-1 1-1h3.5c.6 0 1 .4 1 1 0 1.3.2 2.5.6 3.6.1.3 0 .7-.2 1z"/></svg>555-014-2286</li>
      <li><svg viewBox="0 0 24 24"><path d="M7 1h10a2 2 0 0 1 2 2v18a2 2 0 0 1-2 2H7a2 2 0 0 1-2-2V3a2 2 0 0 1 2-2zm0 3v15h10V4z"/></svg>555-017-4430</li>
    </ul>

    <ul class="contact contact--office">
      <li><svg viewBox="0 0 24 24"><path d="M6 2h12v5H6zM4 8h16a2 2 0 0 1 2 2v7h-4v5H6v-5H2v-7a2 2 0 0 1 2-2zm4 8v4h8v-4z"/></svg>555-019-7712</li>
      <li><svg viewBox="0 0 24 24"><path d="M2 5h20v14H2zm2 2v.5l8 5 8-5V7z"/></svg>hello@alpinecounsel.com</li>
    </ul>

    <div class="rule rule--bottom"></div>
    <ul class="contact address">
      <li><svg viewBox="0 0 24 24"><path d="M12 2a7 7 0 0 1 7 7c0 5-7 13-7 13S5 14 5 9a7 7 0 0 1 7-7zm0 4.5a2.5 2.5 0 1 0 0 5 2.5 2.5 0 0 0 0-5z"/></svg>1240 Linden Court Fairview, Oregon 97024</li>
    </ul>
  </section>
</main>
</body>
</html>
```